Tidewell Electrical Solutions

On one side. LOGO (underneath:) Commercial Industrial Residential

- NAME & CONTACT DETAILS

Martin K. Oduya
Project Manager

(Cell icon) (441) 555-0187
(Email icon) twlelectricalsoultions@mailpost-demo.com
(Facebook & Instagram icons )@twlelectricalsolutions

Other side: LOGO - underneath ELECTRICAL CONSTRUCTION & MAINTENANCE . LED LIGHTING & AUTOMATION . LIFE SAFETY SYSTEMS (FIRE ALARM / SECURITY) . DATA & COMMUNICATION

```html
<!DOCTYPE html>
<html lang="en">
<head>
<meta charset="utf-8">
<title>Tidewell Electrical Solutions – Business Card</title>
<link rel="stylesheet" href="https://fonts.googleapis.com/css2?family=Montserrat:wght@400;500;600;700&family=Lato:wght@400&display=swap">
<style>
  :root {
    --teal: #0b5a7a;
    --ink: #444448;
    --paper: #ffffff;
    --backdrop: #303033;
    --band-text: #ffffff;
  }
  * { box-sizing: border-box; margin: 0; padding: 0; }
  html, body { width: 799px; height: 1200px; overflow: hidden; }
  body {
    background: var(--backdrop);
    font-family: "Montserrat", Arial, sans-serif;
    position: relative;
  }
  .card {
    position: absolute;
    left: 50px;
    width: 700px;
    height: 400px;
    background: var(--paper);
    box-shadow: 0 6px 18px rgba(0,0,0,.45);
    overflow: hidden;
  }
  .card--front { top: 150px; }
  .card--back  { top: 650px; }

  /* brand lockup */
  .brand {
    position: absolute;
    right: 40px;
    top: 38px;
    width: 420px;
  }
  .brand__name {
    display: flex;
    align-items: center;
    gap: 14px;
    justify-content: flex-end;
  }
  .brand__mark {
    width: 54px; height: 54px;
    background: var(--teal);
    flex: none;
  }
  .brand__words {
    font-weight: 600;
    font-size: 22px;
    line-height: 1.05;
    letter-spacing: 3px;
    color: var(--ink);
    text-transform: uppercase;
  }
  .brand__sectors {
    margin-top: 14px;
    text-align: right;
    font-weight: 600;
    font-size: 14px;
    letter-spacing: 2.5px;
    color: var(--teal);
    text-transform: uppercase;
    word-spacing: 6px;
  }

  /* front: services band */
  .services {
    position: absolute;
    left: 0; right: 0;
    top: 188px;
    height: 98px;
    background: var(--teal);
    color: var(--band-text);
    display: flex;
    flex-direction: column;
    justify-content: center;
    padding: 0 36px;
    font-weight: 500;
    font-size: 15px;
    letter-spacing: 0.6px;
    line-height: 1.7;
    text-transform: uppercase;
  }
  .social {
    display: flex;
    align-items: center;
    gap: 8px;
    font-family: "Lato", Arial, sans-serif;
    font-size: 17px;
    color: var(--ink);
  }
  .social__dot {
    width: 18px; height: 18px;
    border: 2px solid var(--teal);
    border-radius: 4px;
    flex: none;
  }
  .card--front .social {
    position: absolute;
    left: 36px;
    top: 318px;
  }

  /* back: contact block */
  .person {
    position: absolute;
    left: 40px;
    top: 168px;
  }
  .person__name {
    font-weight: 700;
    font-size: 23px;
    letter-spacing: 1.5px;
    color: var(--teal);
    text-transform: uppercase;
  }
  .person__role {
    font-size: 15px;
    color: var(--ink);
    margin-top: 2px;
  }
  .contact {
    list-style: none;
    margin-top: 10px;
    font-family: "Lato", Arial, sans-serif;
    font-size: 16px;
    color: var(--ink);
  }
  .contact li { display: flex; align-items: center; gap: 10px; line-height: 1.6; }
  .contact svg { width: 16px; height: 16px; fill: var(--teal); flex: none; }
  .divider {
    position: absolute;
    left: 190px;
    right: 40px;
    top: 232px;
    height: 1.5px;
    background: var(--teal);
  }
  .card--back .social-list {
    position: absolute;
    right: 40px;
    bottom: 40px;
    display: flex;
    flex-direction: column;
    gap: 6px;
    align-items: flex-end;
  }
  .card--back .social { flex-direction: row; }
</style>
</head>
<body>

<section class="card card--front" aria-label="Card front">
  <div class="brand">
    <div class="brand__name">
      <span class="brand__mark" aria-hidden="true"></span>
      <span class="brand__words">Tidewell<br>Electrical<br>Solutions</span>
    </div>
    <p class="brand__sectors">Commercial | Industrial | Residential</p>
  </div>

  <div class="services">
    <p>Electrical Construction &amp; Maintenance | LED Lighting &amp; Automation</p>
    <p>Life Safety Systems (Fire Alarm/Security) | Data &amp; Communication</p>
  </div>

  <div class="social">
    <span class="social__dot" aria-hidden="true"></span>
    <span>@twlelectricalsolutions</span>
  </div>
</section>

<section class="card card--back" aria-label="Card back">
  <div class="brand">
    <div class="brand__name">
      <span class="brand__mark" aria-hidden="true"></span>
      <span class="brand__words">Tidewell<br>Electrical<br>Solutions</span>
    </div>
    <p class="brand__sectors">Commercial | Industrial | Residential</p>
  </div>

  <div class="person">
    <h1 class="person__name">Martin K. Oduya</h1>
    <p class="person__role">Project Manager</p>
    <ul class="contact">
      <li>
        <svg viewBox="0 0 24 24" aria-hidden="true"><path d="M6.6 10.8a15.1 15.1 0 0 0 6.6 6.6l2.2-2.2a1 1 0 0 1 1-.25 11.4 11.4 0 0 0 3.6.57 1 1 0 0 1 1 1V20a1 1 0 0 1-1 1A17 17 0 0 1 3 4a1 1 0 0 1 1-1h3.5a1 1 0 0 1 1 1c0 1.25.2 2.45.57 3.57a1 1 0 0 1-.25 1z"/></svg>
        <span>(441) 555-0187</span>
      </li>
      <li>
        <svg viewBox="0 0 24 24" aria-hidden="true"><path d="M2 5h20v14H2zm2 2v.4l8 5.3 8-5.3V7zm0 2.8V17h16V9.8l-8 5.3z"/></svg>
        <span>twlelectricalsoultions@mailpost-demo.com</span>
      </li>
    </ul>
  </div>

  <div class="divider" aria-hidden="true"></div>

  <div class="social-list">
    <div class="social"><span>@twlelectricalsolutions</span><span class="social__dot" aria-hidden="true"></span></div>
    <div class="social"><span>@twlelectricalsolutions</span><span class="social__dot" aria-hidden="true"></span></div>
  </div>
</section>

</body>
</html>
```